Powepoint template for an investment group

Need high end clear clean concise creative luxurious

Have royal clients
High end/billionaire investors

Using ross gold logo can be creative
Must habe page numbers
Logo preference header top right
Page number footer bottom right

The first page of the ppt maybe a big block of dark grey and oberi investment group written on the front page in rose gold

Target Market(s)

Investors at a high level

Requirements
Must have
• Luxury feel

```html
<!DOCTYPE html>
<html lang="en">
<head>
<meta charset="utf-8">
<title>Oberi Investment Group – Slide 12</title>
<link href="https://fonts.googleapis.com/css2?family=Montserrat:wght@300;400;500;800&display=swap" rel="stylesheet">
<style>
  :root {
    --page-bg: #ffffff;
    --ink: #0c0c0c;
    --body-grey: #c2c2c2;
    --muted-grey: #c4c4c4;
    --rose-gold: #c9a08e;
    --strip-light: #cfcfcf;
    --strip-mid: #8c8c8c;
    --strip-dark: #2e2e2e;
  }
  * { margin: 0; padding: 0; box-sizing: border-box; }
  html, body { width: 1200px; height: 675px; overflow: hidden; background: var(--page-bg); }
  .slide {
    position: relative;
    width: 1200px;
    height: 675px;
    background: var(--page-bg);
    font-family: "Montserrat", sans-serif;
    overflow: hidden;
  }
  .brand {
    position: absolute;
    top: 34px;
    right: 30px;
    font-size: 13px;
    font-weight: 500;
    letter-spacing: 0;
    color: var(--rose-gold);
    white-space: nowrap;
  }
  .photo-strips {
    position: absolute;
    left: 0;
    top: 0;
    width: 680px;
    height: 675px;
  }
  .content {
    position: absolute;
    left: 768px;
    top: 148px;
    width: 362px;
  }
  .eyebrow {
    font-size: 13px;
    font-weight: 500;
    letter-spacing: 3.6px;
    color: var(--ink);
  }
  .title {
    margin-top: 10px;
    font-size: 40px;
    font-weight: 800;
    letter-spacing: 2.4px;
    line-height: 48px;
    color: var(--ink);
  }
  .body-text {
    margin-top: 12px;
    font-size: 13px;
    font-weight: 300;
    line-height: 23.8px;
    color: var(--body-grey);
  }
  .body-text + .body-text { margin-top: 24px; }
  .page-number {
    position: absolute;
    right: 93px;
    top: 636px;
    font-size: 12px;
    font-weight: 300;
    color: var(--muted-grey);
  }
</style>
</head>
<body>
<main class="slide">
  <header class="brand">Oberi Investment Group</header>

  <svg class="photo-strips" viewBox="0 0 680 675" role="img" aria-label="Black and white photograph of glass skyscrapers seen from below, cut into vertical strips">
    <defs>
      <linearGradient id="tower-light" x1="0" y1="0" x2="1" y2="1">
        <stop offset="0" stop-color="#cfcfcf"/>
        <stop offset="1" stop-color="#8c8c8c"/>
      </linearGradient>
      <linearGradient id="tower-mid" x1="0" y1="0" x2="0" y2="1">
        <stop offset="0" stop-color="#b0b0b0"/>
        <stop offset="1" stop-color="#5a5a5a"/>
      </linearGradient>
      <linearGradient id="tower-dark" x1="0" y1="0" x2="1" y2="1">
        <stop offset="0" stop-color="#4a4a4a"/>
        <stop offset="1" stop-color="#2e2e2e"/>
      </linearGradient>
    </defs>
    <rect x="0" y="52" width="141" height="569" fill="url(#tower-light)"/>
    <rect x="150" y="126" width="48" height="430" fill="url(#tower-mid)"/>
    <rect x="206" y="52" width="70" height="569" fill="url(#tower-mid)"/>
    <rect x="285" y="76" width="85" height="525" fill="url(#tower-mid)"/>
    <rect x="379" y="94" width="40" height="485" fill="url(#tower-dark)"/>
    <rect x="428" y="76" width="41" height="538" fill="url(#tower-dark)"/>
    <rect x="477" y="52" width="77" height="549" fill="url(#tower-dark)"/>
    <rect x="562" y="126" width="63" height="458" fill="url(#tower-dark)"/>
    <rect x="634" y="52" width="36" height="569" fill="url(#tower-dark)"/>
  </svg>

  <section class="content">
    <p class="eyebrow">LOREM IPSUM</p>
    <h1 class="title">LOREM<br>IPSUM</h1>
    <p class="body-text">Lorem Ipsum is simply dummy text of the printing and typesetting industry. Lorem Ipsum has been the industry's standard dummy text ever since the 1500s, when an unknown printer took a galley of type and scrambled it to make a type specimen book.</p>
    <p class="body-text">Lorem Ipsum is simply dummy text of the printing and typesetting industry.</p>
  </section>

  <footer class="page-number">12</footer>
</main>
</body>
</html>
```